Professional stationery for an esthetic dentistry, dental implant and oral surgery office
Solvera Dent
Simple
Dr. Θεόδωρος Βαρτσάκης, DDS, MSc
Χειρουργός Οδοντίατρος, MSc in Oral Surgery
Ορφανίδου 9 (= street + Number)
11634 Αθήνα (= PO + City)
vartsakis@solveradent.gr
www.solveradent.gr
The abbreviations on the stationery for tel and mobile number on the front must be as follows:
For tel/fax number= T/F
For mobile= Κ
The greek text explained:
Ορφανίδου 9 (address line 1: street name + street number)
11634 Αθήνα (address line 2: postal code + area)
On the stationery to be displayed also the website address and the email:
On the back I want to be the same but all in english language:
Dr. Theodoros Vartsakis, DDS, MSc
Dentist, MSc in Oral Surgery
The address is:
Orfanidou 9 str.
11634 Athens
Greece
T/F: +30 210 555 0143
M: +30 690 555 0172
Cards that I like
Card that I like

```html
<!DOCTYPE html>
<html lang="el">
<head>
<meta charset="utf-8">
<title>Solvera Dent – Business Cards</title>
<link href="https://fonts.googleapis.com/css2?family=Open+Sans:wght@400;600;700&display=swap" rel="stylesheet">
<style>
  :root {
    --backdrop: #2d2926;
    --card: #4b5a63;
    --card-dark: #3f4d56;
    --text: #ffffff;
    --text-soft: #dfe5e8;
    --accent: #f07a22;
    --accent-dark: #d9621a;
    --silver-light: #eef0f1;
    --silver-dark: #8e969b;
  }
  * { margin: 0; padding: 0; box-sizing: border-box; }
  html, body {
    width: 1200px; height: 614px; overflow: hidden;
    background: var(--backdrop);
    font-family: "Open Sans", Arial, sans-serif;
  }
  .stage { position: relative; width: 1200px; height: 614px; }
  .card {
    position: absolute; top: 172px;
    width: 484px; height: 326px;
    border-radius: 12px; overflow: hidden;
    background: linear-gradient(160deg, var(--card) 0%, var(--card-dark) 100%);
    color: var(--text);
  }
  .card--greek { left: 94px; }
  .card--english { left: 638px; }

  .edge-strip {
    position: absolute; top: 0; right: 0; width: 16px; height: 100%;
    background: var(--card-dark);
  }
  .edge-strip__accent {
    position: absolute; top: 0; left: 0; width: 100%; height: 110px;
    background: linear-gradient(90deg, var(--accent-dark), var(--accent));
  }
  .edge-strip__metal {
    position: absolute; top: 110px; left: 0; width: 100%; height: 82px;
    background: linear-gradient(180deg, var(--silver-light), var(--silver-dark));
  }

  .brand {
    position: absolute; left: 26px; top: 58px;
    display: flex; align-items: center; gap: 10px;
  }
  .brand__dot {
    width: 32px; height: 32px; border-radius: 50%;
    background: var(--text);
  }
  .brand__name {
    font-size: 34px; font-weight: 400; letter-spacing: -0.5px;
    color: var(--text); line-height: 1;
  }

  .doctor {
    position: absolute; right: 40px; top: 128px;
    text-align: right;
  }
  .doctor__name {
    font-size: 15px; font-weight: 700; line-height: 1.3;
  }
  .doctor__title {
    margin-top: 6px;
    font-size: 9.5px; line-height: 1.35; color: var(--text-soft);
  }

  .address {
    position: absolute; left: 26px; top: 140px;
    font-size: 12.5px; line-height: 1.4; color: var(--text);
  }

  .contacts {
    position: absolute; left: 26px; top: 212px;
    list-style: none; font-size: 10.5px; color: var(--text);
  }
  .contacts li {
    display: flex; align-items: center; height: 18px;
  }
  .contacts__label {
    display: inline-block; width: 30px; font-weight: 600;
  }
</style>
</head>
<body>
<div class="stage">

  <!-- Front: Greek -->
  <section class="card card--greek">
    <div class="edge-strip"><div class="edge-strip__accent"></div><div class="edge-strip__metal"></div></div>
    <div class="brand"><span class="brand__dot"></span><span class="brand__name">Solvera Dent</span></div>
    <p class="address">Ορφανίδου 9<br>11634 Αθήνα</p>
    <div class="doctor">
      <p class="doctor__name">Dr. Θεόδωρος Βαρτσάκης,<br>DDS, MSc</p>
      <p class="doctor__title">Χειρουργός Οδοντίατρος,<br>MSc in Oral Surgery</p>
    </div>
    <ul class="contacts">
      <li><span class="contacts__label">T/F:</span><span>+30 210 555 0143</span></li>
      <li><span class="contacts__label">Κ:</span><span>+30 690 555 0172</span></li>
      <li><span class="contacts__label">E:</span><span>vartsakis@solveradent.gr</span></li>
      <li><span class="contacts__label">W:</span><span>www.solveradent.gr</span></li>
    </ul>
  </section>

  <!-- Back: English -->
  <section class="card card--english">
    <div class="edge-strip"><div class="edge-strip__accent"></div><div class="edge-strip__metal"></div></div>
    <div class="brand"><span class="brand__dot"></span><span class="brand__name">Solvera Dent</span></div>
    <p class="address">Orfanidou 9 str.<br>11634 Athens<br>Greece</p>
    <div class="doctor">
      <p class="doctor__name">Dr. Theodoros Vartsakis,<br>DDS, MSc</p>
      <p class="doctor__title">Dentist, MSc in Oral Surgery</p>
    </div>
    <ul class="contacts">
      <li><span class="contacts__label">T/F:</span><span>+30 210 555 0143</span></li>
      <li><span class="contacts__label">M:</span><span>+30 690 555 0172</span></li>
      <li><span class="contacts__label">E:</span><span>vartsakis@solveradent.gr</span></li>
      <li><span class="contacts__label">W:</span><span>www.solveradent.gr</span></li>
    </ul>
  </section>

</div>
</body>
</html>
```